Online Prescription Eyewear Company Needs a Website

We sell prescription glasses starting at $99 with Free Shipping. We have over 300 different styles and colors.

Our website is under construction and we need an amazing landing page to kick things off. Our brand is called VARNO and our website is called VARNOEYEWEAR.EXAMPLE.

We are a website similar to
kestonhale.example
shoprudyplume.example
Brova.example

We sell prescription glasses starting at $99 with Free Shipping. Options to upgrade to Anti Glare, Blue light Protection, Shadeshift or High Index.

We also have a lens replacement option and will change out old prescription lenses starting at $79 with Free Shipping.

Important!!

We Love the layout of https://tessbrundle.example/ . We are hoping to use Tess Brundle as a templet. The closest page that looks like Tess Brundle will win.

We do not prefer the pink. Substitute the pink with Navy Teal.

We also prefer a better footer than Tess Brundle

The landing page should include, Gender neutral and Colors are Black, White, Gray, Navy Teal

We prefer a Simple, Clean Look.

The Header should be similar to kestonhale.example

The Landing page look very similar to Tess Brundle with large banner with quad banner below to follow.

We need better footer. Here are the menu items for footer.

PRODUCTS
All Frames
Mens Frames
Womens Frames
Best Sellers
New Arrivals

ORDER
Single Vision Lenses
Blue Light Blocking Computer Lenses
High Index Lenses
Shadeshift Lenses
Reading Lenses

INFORMATION
Track Order
About Us
Contact Us
Returns
Warranty
FAQ

Target Market(s)

20-40 yo Male/Female wears glasses

Industry/Entity Type

Eyewear

Number of Pages Required

1 page

Font styles to use
Sans Serif

Colors
333333
5c5c5c
919191
b2b2b2
dfdfdf
f5f5f5
1b1b1b
474747
3276b5

Requirements
Must have
• The Landing page look very similar to Tess Brundle.
• Substitute the pink secondary color for Navy Teal
• Should have main Banner with Person wearing glasses. Then the quad banner below should highlight the box with glasses, glasses, etc.
Nice to have
• i have a pixel vault account, so if you find some awesome pictures I can purchase them if they fit in the site.

```html
<!DOCTYPE html>
<html lang="en">
<head>
<meta charset="utf-8">
<title>VARNO — Prescription Eyeglasses</title>
<link href="https://fonts.googleapis.com/css2?family=Montserrat:wght@400;500;600;700&display=swap" rel="stylesheet">
<style>
:root{
  --brand-blue:#3276b5;
  --hero-blue:#5b8fc7;
  --band-blue:#4f7199;
  --footer-blue:#4a84c2;
  --accent:#f5a623;
  --ink:#333333;
  --ink-dark:#1b1b1b;
  --mid:#5c5c5c;
  --soft:#919191;
  --line:#b2b2b2;
  --pale:#dfdfdf;
  --paper:#f5f5f5;
  --white:#ffffff;
}
*{box-sizing:border-box;margin:0;padding:0}
html,body{width:907px;height:1200px;overflow:hidden}
body{position:relative;background:var(--white);font-family:'Montserrat',sans-serif;color:var(--ink)}

/* header */
.site-header{position:absolute;left:0;top:0;width:907px;height:50px;background:var(--white);border-top:2px solid var(--brand-blue)}
.brand{position:absolute;left:177px;top:17px;font-size:14.5px;font-weight:500;letter-spacing:1.5px;color:var(--ink-dark)}
.main-nav{position:absolute;left:244px;top:22px;display:flex}
.main-nav a{font-size:6.5px;font-weight:700;letter-spacing:1px;color:var(--ink);text-decoration:none;padding:0 9px}
.main-nav a.active{border-bottom:1.5px solid var(--accent);padding-bottom:2px}
.nav-marker{position:absolute;left:246px;top:0}
.nav-marker.bottom{top:42px}
.greeting{position:absolute;right:179px;top:5px;font-size:6.5px;color:var(--soft);letter-spacing:.5px}
.greeting b{color:var(--accent);font-weight:600}
.utility{position:absolute;right:179px;top:22px;font-size:6.5px;color:var(--soft);letter-spacing:1px;display:flex;align-items:center;gap:5px}

/* hero */
.hero{position:absolute;left:0;top:50px;width:907px;height:283px;background:var(--hero-blue);overflow:hidden}
.hero-photo{position:absolute;right:0;top:0;width:440px;height:283px;background:radial-gradient(ellipse at 60% 45%,#7ea6d2 0%,#6795c9 45%,var(--hero-blue) 80%)}
.hero-title{position:absolute;left:0;width:710px;top:43px;text-align:center;color:var(--white);font-size:19px;font-weight:700;letter-spacing:3px}
.hero-sub{position:absolute;left:0;width:710px;top:73px;text-align:center;color:var(--white);font-size:11px;font-weight:600;letter-spacing:1.5px}
.hero-sub em{font-style:normal;color:var(--accent)}
.btn-primary{position:absolute;left:258px;top:104px;width:91px;height:20px;background:var(--accent);color:var(--white);font-size:6.5px;font-weight:700;letter-spacing:1px;display:flex;align-items:center;justify-content:center}
.btn-outline{position:absolute;left:359px;top:104px;width:92px;height:20px;border:1px solid #e8b46a;color:var(--white);font-size:7px;letter-spacing:.8px;display:flex;align-items:center;justify-content:center}
.hero-note{position:absolute;left:0;width:710px;top:141px;text-align:center;color:var(--white);font-size:11.5px;font-weight:600;letter-spacing:1.5px}
.arrow{position:absolute;top:97px}

.upgrade-band{position:absolute;left:0;top:213px;width:907px;height:70px;background:rgba(60,88,125,.75)}
.upgrade-title{position:absolute;left:0;width:913px;top:11px;text-align:center;color:var(--white);font-size:11px;font-weight:700;letter-spacing:2px}
.upgrade-options{position:absolute;left:290px;top:33px;display:flex;gap:5px}
.upgrade-options span{width:78px;height:23px;border:1px solid rgba(255,255,255,.85);color:var(--white);font-size:6.5px;font-weight:600;letter-spacing:.8px;display:flex;align-items:center;justify-content:center;text-align:center;line-height:1.3}

/* quad */
.tile{position:absolute;width:267px;height:190px;overflow:hidden}
.tile-photo{position:absolute;inset:0 0 29px 0}
.tile-label{position:absolute;left:0;right:0;bottom:0;height:29px;background:rgba(235,235,235,.92);font-size:8px;font-weight:600;letter-spacing:.8px;color:var(--ink);display:flex;align-items:center;justify-content:center}

/* newsletter */
.newsletter{position:absolute;left:0;top:768px;width:907px;height:189px;background:linear-gradient(90deg,#eceff2 0%,#f7f7f7 40%,#eef0f2 70%,#e4e7ea 100%)}
.join{position:absolute;left:0;width:907px;top:15px;text-align:center;color:var(--brand-blue);font-size:13px;font-weight:700;letter-spacing:2px;text-decoration:underline;text-underline-offset:3px}
.newsletter h2{position:absolute;left:0;width:907px;top:42px;text-align:center;color:var(--ink-dark);font-size:17.5px;font-weight:700;letter-spacing:3px}
.newsletter p{position:absolute;left:0;width:907px;top:76px;text-align:center;color:var(--mid);font-size:9.5px;letter-spacing:2px}
.email{position:absolute;left:245px;top:106px;width:331px;height:28px;border:1px solid var(--line);background:var(--white);font-size:6.5px;font-weight:600;letter-spacing:1.2px;color:var(--mid);display:flex;align-items:center;justify-content:center}
.signup{position:absolute;left:594px;top:106px;width:69px;height:28px;background:var(--accent);color:var(--white);font-size:7.5px;font-weight:700;letter-spacing:1.3px;display:flex;align-items:center;justify-content:center}

/* footer */
.site-footer{position:absolute;left:0;top:957px;width:907px;height:243px;background:var(--footer-blue)}
.footer-brand{position:absolute;left:177px;top:5px;font-size:15px;font-weight:500;letter-spacing:2px;color:rgba(255,255,255,.75)}
.footer-rule{position:absolute;left:0;top:27px;width:907px;height:1px;background:rgba(255,255,255,.55)}
.footer-col{position:absolute;top:36px}
.footer-col h3{font-size:8px;font-weight:700;color:var(--white);letter-spacing:.5px;text-decoration:underline;text-underline-offset:2px;margin-bottom:5px}
.footer-col li{list-style:none;font-size:6.5px;color:var(--white);line-height:11.7px}
.footer-col li.wrap{line-height:8px;padding:2px 0 2px}
.footer-col li.hl{color:var(--accent);font-weight:600}
.social{display:flex;gap:5px;margin-top:2px}
.social span{width:16px;height:16px;border-radius:50%;background:var(--white)}
.social span.on{background:var(--accent)}
.copyright{position:absolute;left:0;width:907px;top:234px;text-align:center;font-size:6px;color:var(--white)}
</style>
</head>
<body>

<header class="site-header">
  <div class="brand">VARNO</div>
  <svg class="nav-marker" width="70" height="6" viewBox="0 0 70 6"><polygon points="0,0 70,0 58,6 12,6" fill="#f5a623"/></svg>
  <svg class="nav-marker bottom" width="70" height="6" viewBox="0 0 70 6"><polygon points="12,0 58,0 70,6 0,6" fill="#f5a623"/></svg>
  <nav class="main-nav">
    <a class="active">EYEGLASSES</a><a>LENSES</a><a>LOCATIONS</a><a>ABOUT US</a><a>CONTACT US</a>
  </nav>
  <div class="greeting">Hello, <b>Marisol</b></div>
  <div class="utility">
    <svg width="9" height="9" viewBox="0 0 10 10"><circle cx="4" cy="4" r="3" fill="none" stroke="#919191" stroke-width="1"/><line x1="6.2" y1="6.2" x2="9" y2="9" stroke="#919191"/></svg>
    SEARCH &nbsp;| &nbsp;HELP
    <svg width="8" height="9" viewBox="0 0 8 9"><rect x="0.5" y="3" width="7" height="5.5" fill="none" stroke="#919191"/><path d="M2.5 3V1.5h3V3" fill="none" stroke="#919191"/></svg>(0)
  </div>
</header>

<section class="hero">
  <div class="hero-photo" role="img" aria-label="Smiling woman wearing tortoiseshell prescription glasses"></div>
  <h1 class="hero-title">PRESCRIPTION EYEGLASSES</h1>
  <div class="hero-sub">Starting at <em>$99</em> with FreeShipping</div>
  <div class="btn-primary">SHOP NOW</div>
  <div class="btn-outline">Check Our Products</div>
  <div class="hero-note">Over 300 Different Styles and Colors</div>
  <svg class="arrow" style="left:176px" width="12" height="20" viewBox="0 0 12 20"><polyline points="10,1 2,10 10,19" fill="none" stroke="#fff" stroke-width="1.5"/></svg>
  <svg class="arrow" style="left:719px" width="12" height="20" viewBox="0 0 12 20"><polyline points="2,1 10,10 2,19" fill="none" stroke="#fff" stroke-width="1.5"/></svg>
  <div class="upgrade-band">
    <div class="upgrade-title">UPGRADABLE TO</div>
    <div class="upgrade-options">
      <span>Anti Glare</span><span>Blue Light<br>Protection</span><span>Shadeshift</span><span>High Index</span>
    </div>
  </div>
</section>

<div class="tile" style="left:177px;top:352px">
  <div class="tile-photo" role="img" aria-label="Woman wearing rose-tinted round sunglasses" style="background:linear-gradient(135deg,#5a4a3e 0%,#a08670 45%,#e7ddd2 100%)"></div>
  <div class="tile-label">BEST SELLERS</div>
</div>
<div class="tile" style="left:463px;top:352px">
  <div class="tile-photo" role="img" aria-label="Wall display of colourful eyeglass frames" style="background:linear-gradient(180deg,#c9c6c4 0%,#dcd9d7 50%,#cfcbc9 100%)"></div>
  <div class="tile-label">ALL PRODUCTS</div>
</div>
<div class="tile" style="left:177px;top:560px">
  <div class="tile-photo" role="img" aria-label="Eyeglasses on a table with a sunlit forest seen through the lenses" style="background:linear-gradient(180deg,#c8b06a 0%,#8f8a4c 50%,#b79c7f 100%)"></div>
  <div class="tile-label">LENS REPLACEMENT</div>
</div>
<div class="tile" style="left:463px;top:560px">
  <div class="tile-photo" role="img" aria-label="Woman in striped blouse wearing dark frame glasses" style="background:linear-gradient(180deg,#b6aea5 0%,#aa9f94 60%,#a8643e 100%)"></div>
  <div class="tile-label">GALLERY</div>
</div>

<section class="newsletter" role="img" aria-label="Soft faded photo of friends in a bright room">
  <div class="join">JOIN TODAY</div>
  <h2>DON’T MISS OUR NEW PRODUCTS!</h2>
  <p>Sign up for our newsletter to be notified of our newest products.</p>
  <div class="email">YOUR EMAIL ADDRESS</div>
  <div class="signup">SIGN UP!</div>
</section>

<footer class="site-footer">
  <div class="footer-brand">VARNO</div>
  <div class="footer-rule"></div>
  <div class="footer-col" style="left:177px">
    <h3>PRODUCTS</h3>
    <ul><li>All Frames</li><li>Mens Frames</li><li>Womens Frames</li><li>Best Sellers</li><li>New Arrivals</li></ul>
  </div>
  <div class="footer-col" style="left:290px">
    <h3>ORDER</h3>
    <ul><li>Single Vision Lenses</li><li class="wrap">Blue Light Blocking<br>Computer Lenses</li><li>High Index Lenses</li><li>Shadeshift Lenses</li><li>Reading Lenses</li></ul>
  </div>
  <div class="footer-col" style="left:413px">
    <h3>INFORMATION</h3>
    <ul><li>Track Order</li><li>About Us</li><li>Contact Us</li><li>Returns</li><li class="hl">Warranty</li><li>FAQ</li></ul>
  </div>
  <div class="footer-col" style="left:648px">
    <h3>KEEP CONNECTED</h3>
    <div class="social"><span class="on"></span><span></span><span></span><span></span></div>
  </div>
  <div class="copyright">©2019 VARNO All Rights Reserved</div>
</footer>

</body>
</html>
```